Double Sided A4 Bi-Fold Brochure - very clear scope included

I have created a package which outlines the design requirements for an A4 brochure which folds twice to a DL size.

I would like whoever works on this project to look at the plant pictures taken in our reception area and use this for inspiration to style the brochure. So incorporate plants into the them/styling.

In the package you will find page layouts. Text outlines. Price schedules. Grouped pictures.

If you have any questions just ask

Thanks

Target Market(s)

Those seeking medical treatment for injury and chronic disease

Industry/Entity Type

Physical Therapy

Colors
acd036
9bcb3b

Requirements
Must have
• Must have a plant theme (not over powering).
• MUST use the green colours in our Logo.
Nice to have
• Use the pictures that we have included in the package where possible

```html
<!DOCTYPE html>
<html lang="en">
<head>
<meta charset="utf-8">
<title>Evenstride Physio – DL Brochure</title>
<link href="https://fonts.googleapis.com/css2?family=Montserrat:wght@400;500;600;700&display=swap" rel="stylesheet">
<style>
  :root {
    --green: #acd036;
    --green-deep: #9bcb3b;
    --green-dark: #6fb52c;
    --ink: #2b2b2b;
    --body: #6a6a6a;
    --muted: #9a9a9a;
    --paper: #ffffff;
    --surface: #ebebeb;
  }
  * { box-sizing: border-box; margin: 0; padding: 0; }
  html, body { width: 1200px; height: 1200px; overflow: hidden; }
  body {
    background: var(--surface);
    font-family: "Montserrat", sans-serif;
    position: relative;
  }
  .panel {
    position: absolute;
    top: 100px;
    width: 480px;
    height: 1000px;
    background: var(--paper);
    box-shadow: 0 2px 10px rgba(0,0,0,0.08);
    overflow: hidden;
  }
  .panel-back { left: 90px; }
  .panel-front { left: 630px; }
  .panel-art { position: absolute; inset: 0; }

  /* Back panel */
  .intro { position: absolute; top: 56px; left: 44px; right: 44px; }
  .intro-title {
    font-size: 24px; font-weight: 600; letter-spacing: 1.5px;
    color: var(--ink); margin-bottom: 18px;
  }
  .intro-text { font-size: 15px; line-height: 1.65; color: var(--body); }
  .team {
    position: absolute; top: 330px; left: 44px; right: 44px;
    display: flex; gap: 60px;
  }
  .member { width: 150px; text-align: center; }
  .member-photo {
    width: 140px; height: 140px; border-radius: 50%;
    border: 7px dotted var(--green);
    padding: 6px; margin: 0 auto 16px;
  }
  .member-photo span {
    display: block; width: 100%; height: 100%; border-radius: 50%;
    background: linear-gradient(160deg, #dfe6ea, #a9b4bb);
  }
  .member-name { font-size: 16px; color: var(--muted); }

  /* Brand lockup */
  .brand {
    position: absolute; display: flex; align-items: center; gap: 12px;
    color: var(--green-dark); font-weight: 600; line-height: 0.95;
  }
  .brand-dot { border-radius: 50%; background: var(--green); flex: none; }
  .brand-back { left: 110px; bottom: 70px; font-size: 34px; }
  .brand-back .brand-dot { width: 20px; height: 20px; }
  .brand-front { left: 140px; top: 745px; font-size: 46px; }
  .brand-front .brand-dot { width: 24px; height: 24px; }

  /* Front panel */
  .phone {
    position: absolute; top: 58px; right: 44px;
    font-size: 30px; font-weight: 500; color: var(--ink); letter-spacing: 1px;
  }
  .web {
    position: absolute; top: 885px; left: 120px; width: 320px;
    padding: 12px 0; border-radius: 30px; text-align: center;
    background: var(--green); color: #fff; font-size: 15px; font-weight: 600;
  }
</style>
</head>
<body>

<section class="panel panel-back">
  <svg class="panel-art" viewBox="0 0 480 1000" width="480" height="1000">
    <defs>
      <linearGradient id="mapTone" x1="0" y1="0" x2="0" y2="1">
        <stop offset="0" stop-color="#f4f8ea"/>
        <stop offset="1" stop-color="#e3efc8"/>
      </linearGradient>
    </defs>
    <rect x="44" y="540" width="392" height="220" rx="6" fill="url(#mapTone)" role="img" aria-label="Street map showing the clinic location near Harbour St, The Esplanade and Kestrel Rd"/>
    <path d="M0 820 Q260 800 480 690" fill="none" stroke="var(--green-deep)" stroke-width="9"/>
    <path d="M0 836 Q260 816 480 706" fill="none" stroke="var(--green)" stroke-width="3" opacity="0.6"/>
  </svg>

  <div class="intro">
    <h2 class="intro-title">FAMILY PHYSIO</h2>
    <p class="intro-text">Evenstride Physio is a family business that combines the highest calibre of health professionals with a genuine commitment to supporting our community. Sincere and genuine care for our patients is valued before anything else in our clinic and we pride ourselves on making you feel comfortable.</p>
  </div>

  <div class="team">
    <figure class="member">
      <div class="member-photo" role="img" aria-label="Portrait photo of physiotherapist Maren Ellis"><span></span></div>
      <figcaption class="member-name">Maren Ellis</figcaption>
    </figure>
    <figure class="member">
      <div class="member-photo" role="img" aria-label="Portrait photo of physiotherapist Tessa Grove"><span></span></div>
      <figcaption class="member-name">Tessa Grove</figcaption>
    </figure>
  </div>

  <div class="brand brand-back"><span class="brand-dot"></span><span>evenstride<br>physio</span></div>
</section>

<section class="panel panel-front">
  <svg class="panel-art" viewBox="0 0 480 1000" width="480" height="1000">
    <defs>
      <linearGradient id="heroTone" x1="0" y1="0" x2="0.6" y2="1">
        <stop offset="0" stop-color="#f3f6f7"/>
        <stop offset="0.55" stop-color="#c9dfa0"/>
        <stop offset="1" stop-color="#8fbf45"/>
      </linearGradient>
    </defs>
    <path d="M0 130 H480 V560 Q200 600 0 800 Z" fill="url(#heroTone)" role="img" aria-label="Photo of a smiling older couple outdoors, the woman riding piggyback on the man in a green polo shirt"/>
    <path d="M0 800 Q200 600 480 560" fill="none" stroke="var(--green-deep)" stroke-width="9"/>
    <path d="M0 818 Q205 618 480 578" fill="none" stroke="var(--green)" stroke-width="3" opacity="0.6"/>
  </svg>

  <div class="phone">(80) 5550 1840</div>
  <div class="brand brand-front"><span class="brand-dot"></span><span>evenstride<br>physio</span></div>
  <div class="web">www.evenstridephysio.com.au</div>
</section>

</body>
</html>
```